Business Card Design

Looking for business card designs for a new business. there will be two cards of the same design (both lots of information below in contact info). We would like the logo diagonally across the card with the information split above and below the logo similar to sketch. happy to look at similar alternatives
Please use same colours as in logo design

Industry/Entity Type

Business

Contact Information for Business Card

Gareth Mullins
mob - 0498 172 309
ph - 02 4839 2100
fax - 02 4839 2400
email - gaz@ridgelinetrusses.com.au
14 Calloway Road, Parrinda NSW 2340

Desmond Alcott
mob - 0426 918 753
ph - 02 4839 2100
fax - 02 4839 2400
email - desmond@ridgelinetrusses.com.au

```html
<!DOCTYPE html>
<html lang="en">
<head>
<meta charset="utf-8">
<title>Ridgeline Trusses – Business Cards</title>
<link href="https://fonts.googleapis.com/css2?family=Questrial&display=swap" rel="stylesheet">
<style>
  :root {
    --teal: #077a7d;
    --charcoal: #343434;
    --white: #ffffff;
    --page: #f4f4f4;
  }
  * { box-sizing: border-box; margin: 0; padding: 0; }
  html, body {
    width: 1200px;
    height: 1000px;
    overflow: hidden;
    background: var(--page);
    font-family: "Questrial", "Century Gothic", sans-serif;
  }
  .sheet { position: relative; width: 1200px; height: 1000px; }

  .card {
    position: absolute;
    width: 660px;
    height: 400px;
    background: var(--teal);
    overflow: hidden;
    color: var(--white);
    box-shadow: 0 6px 18px rgba(0,0,0,0.18);
  }
  .card--first { left: 100px; top: 60px; }
  .card--second { left: 440px; top: 540px; }

  .card__band { position: absolute; inset: 0; width: 660px; height: 400px; }

  .card__person {
    position: absolute;
    left: 36px;
    top: 34px;
  }
  .card__name {
    font-size: 19px;
    letter-spacing: 1.5px;
    text-transform: uppercase;
    margin-bottom: 6px;
  }
  .contact-line {
    display: flex;
    align-items: center;
    gap: 7px;
    font-size: 16px;
    line-height: 25px;
  }
  .contact-line svg { width: 18px; height: 16px; flex: none; }

  .card__office {
    position: absolute;
    right: 38px;
    bottom: 36px;
    text-align: right;
  }
  .card__office .contact-line { justify-content: flex-end; font-size: 19px; line-height: 29px; }
  .card__office .contact-line svg { width: 20px; height: 18px; }
  .card__address { font-size: 18px; margin-top: 6px; }

  .card__brand {
    position: absolute;
    left: 330px;
    top: 205px;
    transform: translate(-50%, -50%) rotate(-20.8deg);
    font-size: 58px;
    color: var(--charcoal);
    white-space: nowrap;
    letter-spacing: 0.5px;
  }
</style>
</head>
<body>
<main class="sheet">

  <article class="card card--first">
    <svg class="card__band" viewBox="0 0 660 400" aria-hidden="true">
      <polygon points="0,249 660,-11 660,0 0,260" fill="var(--charcoal)"/>
      <polygon points="0,260 660,0 660,160 0,400" fill="var(--white)"/>
      <polygon points="0,400 660,160 660,171 0,411" fill="var(--charcoal)"/>
    </svg>
    <div class="card__person">
      <p class="card__name">Gareth Mullins</p>
      <p class="contact-line">
        <svg viewBox="0 0 20 18"><rect x="1" y="1" width="18" height="16" rx="2" fill="var(--white)"/><rect x="7" y="3" width="6" height="12" rx="1" fill="var(--teal)"/></svg>
        0498 172 309
      </p>
      <p class="contact-line">
        <svg viewBox="0 0 20 18"><rect x="1.5" y="3" width="17" height="12" fill="none" stroke="var(--white)" stroke-width="2"/><polyline points="2,4 10,10 18,4" fill="none" stroke="var(--white)" stroke-width="2"/></svg>
        gaz@ridgelinetrusses.com.au
      </p>
    </div>
    <div class="card__brand">Ridgeline Trusses</div>
    <div class="card__office">
      <p class="contact-line">
        <svg viewBox="0 0 20 18"><rect x="1" y="1" width="18" height="16" rx="2" fill="var(--white)"/><path d="M6 4 Q4 9 9 14 L11 12 L9 10 Q8 8 9 7 L7 5 Z" fill="var(--teal)"/></svg>
        02 4839 2100
      </p>
      <p class="contact-line">
        <svg viewBox="0 0 20 18"><rect x="1" y="1" width="18" height="16" rx="2" fill="var(--white)"/><rect x="4" y="4" width="12" height="3" fill="var(--teal)"/><rect x="4" y="9" width="12" height="5" fill="var(--teal)"/></svg>
        02 4839 2400
      </p>
      <p class="card__address">14 Calloway Road, Parrinda NSW 2340</p>
    </div>
  </article>

  <article class="card card--second">
    <svg class="card__band" viewBox="0 0 660 400" aria-hidden="true">
      <polygon points="0,249 660,-11 660,0 0,260" fill="var(--charcoal)"/>
      <polygon points="0,260 660,0 660,160 0,400" fill="var(--white)"/>
      <polygon points="0,400 660,160 660,171 0,411" fill="var(--charcoal)"/>
    </svg>
    <div class="card__person">
      <p class="card__name">Desmond Alcott</p>
      <p class="contact-line">
        <svg viewBox="0 0 20 18"><rect x="1" y="1" width="18" height="16" rx="2" fill="var(--white)"/><rect x="7" y="3" width="6" height="12" rx="1" fill="var(--teal)"/></svg>
        0426 918 753
      </p>
      <p class="contact-line">
        <svg viewBox="0 0 20 18"><rect x="1.5" y="3" width="17" height="12" fill="none" stroke="var(--white)" stroke-width="2"/><polyline points="2,4 10,10 18,4" fill="none" stroke="var(--white)" stroke-width="2"/></svg>
        desmond@ridgelinetrusses.com.au
      </p>
    </div>
    <div class="card__brand">Ridgeline Trusses</div>
    <div class="card__office">
      <p class="contact-line">
        <svg viewBox="0 0 20 18"><rect x="1" y="1" width="18" height="16" rx="2" fill="var(--white)"/><path d="M6 4 Q4 9 9 14 L11 12 L9 10 Q8 8 9 7 L7 5 Z" fill="var(--teal)"/></svg>
        02 4839 2100
      </p>
      <p class="contact-line">
        <svg viewBox="0 0 20 18"><rect x="1" y="1" width="18" height="16" rx="2" fill="var(--white)"/><rect x="4" y="4" width="12" height="3" fill="var(--teal)"/><rect x="4" y="9" width="12" height="5" fill="var(--teal)"/></svg>
        02 4839 2400
      </p>
      <p class="card__address">14 Calloway Road, Parrinda NSW 2340</p>
    </div>
  </article>

</main>
</body>
</html>
```